brightOn Journal. Zest+Ease for Lively Elders 50+ in the San Francisco Bay Area

I don't need a logo. I will upload the design. OK to play with the colors. I need a website that conveys warmth, elegance, vibrancy and fun. Our website will give a home to this digital magazine. I also need the following:<br/>About Us<br/>Community Calendar<br/>Resources<br/>Blog<br/>Donate (we are a nonprofit)<br/>Contact Us.<br/>We will use Wordpress. <br/><br/>Videos will be added<br/><br/>Store for products will be included

```html
<!DOCTYPE html>
<html lang="en">
<head>
<meta charset="utf-8">
<title>brightOn Journal</title>
<link href="https://fonts.googleapis.com/css2?family=Oswald:wght@500;600;700&family=Poppins:wght@400;500;600;700&display=swap" rel="stylesheet">
<style>
:root{
  --yellow:#fdf36c;
  --yellow-deep:#f7e94a;
  --ink:#141414;
  --grey-text:#7d7d7d;
  --grey-title:#9a9a9a;
  --panel:#f1f1f1;
  --white:#ffffff;
  --line:#e2e2e2;
  --head:'Oswald',sans-serif;
  --body:'Poppins',sans-serif;
}
*{box-sizing:border-box;margin:0;padding:0}
html,body{width:1200px;height:5244px;overflow:hidden}
body{position:relative;background:var(--white);font-family:var(--body);color:var(--ink)}
.abs{position:absolute}
p{font-size:13px;line-height:1.75;color:var(--grey-text)}
.btn{display:inline-block;font-family:var(--body);font-weight:600;font-size:10px;letter-spacing:.08em;text-transform:uppercase;padding:7px 18px;border-radius:20px}
.btn-yellow{background:var(--yellow);color:var(--ink)}
.btn-dark{background:var(--ink);color:var(--white)}
.btn-ghost{border:1.5px solid var(--white);color:var(--white)}
.btn-outline{border:1.5px solid var(--ink);color:var(--ink)}

/* header */
.site-header{top:0;left:0;width:1200px;height:72px;background:var(--white);z-index:5}
.brand{left:150px;top:14px}
.brand-name{font-family:var(--body);font-weight:700;font-size:26px;line-height:1;color:var(--ink)}
.brand-tag{font-size:7.5px;color:var(--grey-text);margin-top:3px}
.main-nav{right:150px;top:0;display:flex;align-items:center;height:50px;gap:22px;font-size:12px;font-weight:500}
.main-nav .current{background:var(--yellow);padding:17px 14px}
.main-nav .btn{padding:6px 16px;font-size:9.5px}

/* hero */
.hero{top:0;left:0;width:1200px;height:650px;background:linear-gradient(90deg,#1a1d17 0%,#3a4636 35%,#8fa07a 65%,#c9c5a4 100%);clip-path:polygon(0 0,100% 0,100% 92%,0 100%)}
.hero-copy{left:150px;top:235px;color:var(--white)}
.hero-copy .kicker{font-family:var(--head);font-size:30px;font-weight:500}
.hero-copy h1{font-family:var(--head);font-size:72px;font-weight:700;line-height:1;margin:2px 0 14px}
.hero-copy p{color:#ddd;font-size:11px;width:280px;line-height:1.6;margin-bottom:26px}
.hero-dot{left:596px;top:612px;width:9px;height:9px;border-radius:50%;background:var(--white)}

/* about */
.about-block{left:0;top:700px;width:400px;height:520px;background:var(--yellow)}
.about-photo{left:75px;top:710px;width:400px;height:410px;background:linear-gradient(160deg,#8ea36c,#c9b79a 55%,#6b7c8f)}
.about-copy{left:550px;top:780px;width:500px}
.about-copy h2{font-family:var(--head);font-size:70px;font-weight:700;line-height:1.1;margin-bottom:18px}
.about-copy p{margin-bottom:14px}

/* calendar */
.cal-band{left:0;top:1230px;width:1200px;height:1270px;background:var(--panel);clip-path:polygon(0 4%,100% 0,100% 100%,0 100%)}
.cal-title{left:150px;top:1460px;font-family:var(--head);font-size:74px;font-weight:700;line-height:1}
.cal-title .soft{color:var(--grey-title)}
.cal-intro{left:580px;top:1455px;width:470px}
.cal-intro h3{font-family:var(--body);font-size:17px;font-weight:600;margin-bottom:14px}
.cal-card{left:130px;top:1745px;width:990px;height:595px;background:var(--white);box-shadow:0 10px 40px rgba(0,0,0,.08)}
.calendar{left:20px;top:85px;width:540px;border-collapse:collapse;font-size:11px}
.cal-head{background:var(--yellow);height:40px}
.cal-head td{padding:0 18px;font-weight:600;font-size:13px}
.cal-head .nav{text-align:right;font-size:14px;letter-spacing:8px}
.calendar th{background:#bdbdbd;color:var(--white);font-weight:500;height:26px;font-size:10px}
.calendar td.d{height:64px;text-align:center;border:1px solid var(--line);color:#555}
.calendar td.hi{background:var(--yellow)}
.events{left:570px;top:85px;width:345px}
.events-head{background:var(--yellow);border-radius:20px;padding:11px 18px;font-weight:600;font-size:13px;margin-bottom:20px}
.event{display:flex;gap:12px;margin-bottom:22px}
.event-photo{width:160px;height:130px;flex:none}
.event p{font-size:9.5px;line-height:1.5}
.event .date{font-size:9px;margin:6px 0 10px;color:var(--ink)}
.event .more{font-size:10px;font-weight:600;display:flex;align-items:center;gap:10px}
.pager{left:570px;top:503px;display:flex;gap:8px}
.pager span{width:20px;height:20px;border-radius:50%;border:1px solid #bbb;display:flex;align-items:center;justify-content:center}
.pager span.on{background:var(--ink);border-color:var(--ink)}

/* video */
.video-side{top:2490px;width:115px;height:500px;background:linear-gradient(180deg,#b8c4b0,#7f9364);opacity:.55}
.video-main{left:150px;top:2490px;width:900px;height:500px;background:linear-gradient(170deg,#9fb27c 0%,#6f8a4b 55%,#4e6a2f 100%)}
.play{left:573px;top:2712px;width:56px;height:56px;border-radius:50%;background:var(--white);display:flex;align-items:center;justify-content:center}

/* resources */
.res-band{left:0;top:2990px;width:1200px;height:890px;background:var(--yellow);clip-path:polygon(0 0,100% 0,100% 100%,0 90%)}
.res-title{left:0;top:3130px;width:1200px;text-align:center}
.res-title h2{font-family:var(--head);font-size:72px;font-weight:700}
.res-title p{width:660px;margin:10px auto 0;color:#555;font-size:11px}
.res-card{top:3380px;width:430px;height:260px}
.res-cover{left:0;top:0;width:175px;height:230px}
.res-info{left:110px;top:10px;width:300px;height:250px;background:var(--white);padding:28px 28px 0 80px;box-shadow:0 8px 30px rgba(0,0,0,.08)}
.res-info h4{font-size:15px;font-weight:600}
.stars{color:#f2b900;font-size:12px;letter-spacing:2px;margin:6px 0 8px}
.res-info p{font-size:9.5px;line-height:1.6}
.res-info .btn{position:absolute;left:90px;bottom:-14px}
.arrow{top:3525px;width:32px;height:32px;border-radius:50%;display:flex;align-items:center;justify-content:center}

/* blogs */
.blog-title{left:150px;top:3990px;font-family:var(--head);font-size:72px;font-weight:700;line-height:1}
.blog-title .soft{color:var(--grey-title)}
.blog-copy{left:150px;top:4090px;width:360px}
.blog-copy .btn{margin-top:20px}
.blog-post{top:4020px;width:180px}
.blog-photo{height:232px}
.blog-post p{font-size:9px;line-height:1.5;margin:10px 0 8px}

/* cta + footer */
.footer{left:0;top:4540px;width:1200px;height:704px;background:var(--ink);clip-path:polygon(0 16%,100% 0,100% 100%,0 100%)}
.cta{left:150px;top:4460px;width:900px;height:310px;background:var(--white);box-shadow:0 10px 40px rgba(0,0,0,.1);text-align:center;padding-top:110px}
.cta h3{font-size:28px;font-weight:700}
.cta p{font-size:11px;width:480px;margin:14px auto 22px;line-height:1.6}
.foot-col{top:4940px;color:var(--white)}
.foot-col h5{font-size:14px;font-weight:600;margin-bottom:22px}
.foot-col li{list-style:none;font-size:11px;margin-bottom:9px;color:#ddd}
.foot-email{font-size:11px;color:#ddd;line-height:1.6}
.foot-email b{color:var(--yellow);font-weight:500}
.socials{display:flex;gap:8px;margin-top:18px}
.socials span{width:22px;height:22px;border-radius:50%}
.foot-divider{left:150px;top:5100px;width:900px;height:1px;background:#444}
.field{border:1px solid #666;border-radius:16px;height:26px;width:300px;margin-bottom:10px;font-size:9px;color:#aaa;padding:7px 14px}
.field.msg{height:80px;border-radius:12px}
.send{left:950px;top:5060px;width:30px;height:30px;background:var(--yellow);font-size:9px;font-weight:600;display:flex;align-items:center;justify-content:center}
.copyright{left:150px;top:5125px;font-size:10px;color:#bbb}
</style>
</head>
<body>

<div class="abs hero" role="img" aria-label="Photo of an active older couple jogging outdoors on a green park path"></div>

<header class="abs site-header">
  <div class="abs brand">
    <div class="brand-name">brightOn</div>
    <div class="brand-tag">Zest+Ease for Lively Elders 50+</div>
  </div>
  <nav class="abs main-nav">
    <span class="current">Home</span>
    <span>About Us</span>
    <span>Community Calendar</span>
    <span>Resources</span>
    <span>Blog</span>
    <span class="btn btn-dark">Contact Us</span>
    <span class="btn btn-yellow">Donate</span>
  </nav>
</header>

<section class="abs hero-copy">
  <div class="kicker">Welcome To</div>
  <h1>brightOn</h1>
  <p>A lively home for stories, events and ideas that keep life bright after fifty.</p>
  <span class="btn btn-ghost">Explore More</span>
</section>
<div class="abs hero-dot"></div>

<!-- About -->
<div class="abs about-block"></div>
<div class="abs about-photo" role="img" aria-label="Photo of a smiling grandfather carrying his granddaughter on his shoulders"></div>
<section class="abs about-copy">
  <h2>About Us</h2>
  <p>brightOn Journal is a nonprofit digital magazine for people over fifty in the Bay Area. We share stories of health, travel, learning and friendship, and we gather our readers around events that spark joy and keep the whole community moving forward together every season.</p>
  <p>We began as a small newsletter shared by neighbours and grew into a journal read across the region, built by volunteers who believe every chapter of life deserves warmth, style and plenty of fun.</p>
  <span class="btn btn-yellow" style="margin-top:10px">View More</span>
</section>

<!-- Community Calendar -->
<div class="abs cal-band"></div>
<h2 class="abs cal-title"><span class="soft">Community</span><br>Calendar</h2>
<section class="abs cal-intro">
  <h3>Find Something Fun This Month</h3>
  <p>Walks, classes, concerts and volunteer days across the Bay Area, chosen for curious minds and active bodies. Browse the dates below, pick an event that suits you and bring a friend along, because every gathering is friendlier with a familiar face and there is always room for one more at the table.</p>
</section>

<div class="abs cal-card">
  <table class="abs calendar">
    <tr class="cal-head"><td colspan="4">March, 2020</td><td colspan="3" class="nav">‹ ›</td></tr>
    <tr><th>Su</th><th>Mo</th><th>Tu</th><th>We</th><th>Th</th><th>Fr</th><th>Sa</th></tr>
    <tr><td class="d">1</td><td class="d">2</td><td class="d">3</td><td class="d">4</td><td class="d">5</td><td class="d">6</td><td class="d">7</td></tr>
    <tr><td class="d">8</td><td class="d">9</td><td class="d hi">10</td><td class="d">11</td><td class="d">12</td><td class="d">13</td><td class="d">14</td></tr>
    <tr><td class="d">15</td><td class="d">16</td><td class="d">17</td><td class="d">18</td><td class="d">19</td><td class="d">20</td><td class="d">21</td></tr>
    <tr><td class="d">22</td><td class="d">23</td><td class="d">24</td><td class="d hi">25</td><td class="d">26</td><td class="d">27</td><td class="d">28</td></tr>
    <tr><td class="d">29</td><td class="d">30</td><td class="d">31</td><td class="d"></td><td class="d"></td><td class="d"></td><td class="d"></td></tr>
  </table>
  <div class="abs events">
    <div class="events-head">Community Events</div>
    <div class="event">
      <div class="event-photo" role="img" aria-label="Photo of a group of older friends laughing together outdoors" style="background:linear-gradient(150deg,#c7a07a,#8f6c52)"></div>
      <div>
        <p>Morning walk and coffee meetup along the bay trail for all paces.</p>
        <div class="date">10 March, 2020</div>
        <div class="more">View Event <svg width="26" height="8" viewBox="0 0 26 8"><path d="M0 4h24M20 1l4 3-4 3" stroke="#141414" fill="none" stroke-width="1.2"/></svg></div>
      </div>
    </div>
    <div class="event">
      <div class="event-photo" role="img" aria-label="Photo of a grandparent and grandchildren playing in a park" style="background:linear-gradient(150deg,#a8c1d8,#7c9a6a)"></div>
      <div>
        <p>Spring garden workshop with planting tips and a picnic lunch.</p>
        <div class="date">25 March, 2020</div>
        <div class="more">View Event <svg width="26" height="8" viewBox="0 0 26 8"><path d="M0 4h24M20 1l4 3-4 3" stroke="#141414" fill="none" stroke-width="1.2"/></svg></div>
      </div>
    </div>
  </div>
  <div class="abs pager">
    <span><svg width="8" height="8" viewBox="0 0 8 8"><path d="M5 1L2 4l3 3" stroke="#888" fill="none"/></svg></span>
    <span class="on"><svg width="8" height="8" viewBox="0 0 8 8"><path d="M3 1l3 3-3 3" stroke="#fff" fill="none"/></svg></span>
  </div>
</div>

<!-- Video -->
<div class="abs video-side" style="left:0"></div>
<div class="abs video-side" style="left:1085px"></div>
<div class="abs video-main" role="img" aria-label="Video still of a grandfather and grandson running across a grassy field"></div>
<div class="abs play"><svg width="16" height="18" viewBox="0 0 16 18"><path d="M2 1l13 8-13 8z" fill="#141414"/></svg></div>

<!-- Resources -->
<div class="abs res-band"></div>
<section class="abs res-title">
  <h2>Resources</h2>
  <p>Guides, back issues and trusted services gathered by our editors to help you stay healthy, connected and curious. Read online, share with friends, or order a printed copy for someone who loves turning real pages.</p>
</section>
<div class="abs arrow" style="left:55px;background:var(--white)"><svg width="10" height="10" viewBox="0 0 10 10"><path d="M6 2L3 5l3 3" stroke="#141414" fill="none" stroke-width="1.5"/></svg></div>
<div class="abs arrow" style="left:1110px;background:var(--ink)"><svg width="10" height="10" viewBox="0 0 10 10"><path d="M4 2l3 3-3 3" stroke="#fff" fill="none" stroke-width="1.5"/></svg></div>

<div class="abs res-card" style="left:150px">
  <div class="abs res-info">
    <h4>Sed Ut Perspiciatis</h4>
    <div class="stars">★★★★★</div>
    <p>Our spring issue on travel close to home, with easy day trips, local guides and readers' favourite hidden spots.</p>
    <span class="btn btn-dark">Explore More</span>
  </div>
  <div class="abs res-cover" role="img" aria-label="Magazine cover photo of an older couple on the beach" style="background:linear-gradient(170deg,#5c7fb0,#c7b28f)"></div>
</div>
<div class="abs res-card" style="left:620px">
  <div class="abs res-info">
    <h4>Sed Ut Perspiciatis</h4>
    <div class="stars">★★★☆☆</div>
    <p>Our summer issue on staying active, with gentle workouts, dance nights and stories of friends who move together.</p>
    <span class="btn btn-dark">Explore More</span>
  </div>
  <div class="abs res-cover" role="img" aria-label="Magazine cover photo of a joyful older couple outdoors" style="background:linear-gradient(170deg,#2b58a8,#e7c24b)"></div>
</div>

<!-- Recent Blogs -->
<h2 class="abs blog-title"><span class="soft">Recent</span> Blogs</h2>
<section class="abs blog-copy">
  <p>Fresh writing from our community of readers and editors, full of ideas for living well, trying new things and keeping good company.</p>
  <span class="btn btn-outline">All Blogs</span>
</section>
<article class="abs blog-post" style="left:630px">
  <div class="blog-photo" role="img" aria-label="Photo of a city street at night" style="background:linear-gradient(170deg,#2a2421,#6b4a2c)"></div>
  <p>Evening strolls and the best spots for a quiet dinner downtown.</p>
  <svg width="60" height="8" viewBox="0 0 60 8"><path d="M0 4h58M54 1l4 3-4 3" stroke="#141414" fill="none" stroke-width="1.2"/></svg>
</article>
<article class="abs blog-post" style="left:830px">
  <div class="blog-photo" role="img" aria-label="Photo of city buildings on a cloudy day" style="background:linear-gradient(170deg,#9aa3ad,#4e5358)"></div>
  <p>A slow weekend guide to galleries, cafés and rooftop views.</p>
  <svg width="60" height="8" viewBox="0 0 60 8"><path d="M0 4h58M54 1l4 3-4 3" stroke="#141414" fill="none" stroke-width="1.2"/></svg>
</article>
<article class="abs blog-post" style="left:1030px;width:170px;overflow:hidden">
  <div class="blog-photo" role="img" aria-label="Photo of a busy shopping street" style="background:linear-gradient(170deg,#8b6f5d,#3d3530)"></div>
  <p>Market mornings and the joy of local shops.</p>
  <svg width="60" height="8" viewBox="0 0 60 8"><path d="M0 4h58M54 1l4 3-4 3" stroke="#141414" fill="none" stroke-width="1.2"/></svg>
</article>

<!-- Footer -->
<div class="abs footer"></div>
<section class="abs cta">
  <h3>Help Us Keep Life Bright</h3>
  <p>brightOn Journal is a nonprofit. Your gift keeps our stories free and our community events open to everyone.</p>
  <span class="btn btn-yellow">Donate</span>
</section>

<div class="abs foot-col" style="left:150px">
  <h5>Quick Links</h5>
  <ul><li>Home</li><li>About Us</li><li>Community Calendar</li><li>Resources</li><li>Blog</li></ul>
</div>
<div class="abs foot-col" style="left:365px">
  <h5>Others</h5>
  <div class="foot-email"><b>Email</b><br>hello@brightonjournal.org</div>
  <div class="socials">
    <span style="background:#3b5bab"></span>
    <span style="background:#2aa2e0"></span>
    <span style="background:#c8358d"></span>
    <span style="background:#2f7bb8"></span>
  </div>
</div>
<div class="abs foot-col" style="left:695px">
  <h5>Contact</h5>
  <div class="field">Name</div>
  <div class="field">Email</div>
  <div class="field">Phone No</div>
  <div class="field msg">Message</div>
</div>
<div class="abs send">GO</div>
<div class="abs foot-divider"></div>
<div class="abs copyright">Copyright © 2020 brightOn, All Rights Reserved</div>

</body>
</html>
```